Product Line - Label & Logo design

Logo & label design for a supplement line we are developing . The product name is BROVEN ( qtz ) We would like a white jar with a purple metalic lid and somehow blend in the lettering/wording . I will attach sample products to view. Feel free to add in the boxes of the label with the numbers from the sample label. We can correct once we have the design completed. Feel free to change the lettering style, shape etc

Target Market(s)

Supplement / exercise

Industry/Entity Type

Fitness

Colors
6B429C
8869AF
B7A5CE
E3DAEB
F3F0F8

```html
<!DOCTYPE html>
<html lang="en">
<head>
<meta charset="utf-8">
<title>BROVEN Pre Workout – Label</title>
<link href="https://fonts.googleapis.com/css2?family=Exo+2:ital,wght@0,800;0,900;1,800;1,900&family=Montserrat:wght@400;600;700&family=Oswald:wght@700&display=swap" rel="stylesheet">
<style>
  :root{
    --purple:#8c15a9;
    --purple-bright:#a61fc7;
    --ink:#0d0d0f;
    --carbon:#19191c;
    --white:#ffffff;
    --lime:#c9e23b;
  }
  *{margin:0;padding:0;box-sizing:border-box}
  html,body{width:864px;height:1200px;overflow:hidden;background:var(--white)}
  .canvas{position:relative;width:864px;height:1200px;background:var(--white)}
  .label{
    position:absolute;left:20px;top:377px;width:824px;height:446px;overflow:hidden;
    background:
      repeating-linear-gradient(135deg,rgba(255,255,255,.035) 0 2px,transparent 2px 6px),
      var(--carbon);
    font-family:"Montserrat",sans-serif;color:var(--white);
  }
  .label-shapes{position:absolute;inset:0;width:824px;height:446px}

  .brand-name{
    position:absolute;font-family:"Exo 2",sans-serif;font-weight:900;color:var(--white);
    letter-spacing:3px;line-height:1;
  }
  .brand-top{left:298px;top:17px;font-size:38px}
  .brand-bottom{left:608px;top:336px;font-size:34px}

  .product-pre{
    position:absolute;left:262px;top:86px;width:300px;text-align:center;
    font-family:"Exo 2",sans-serif;font-weight:900;font-style:italic;
    font-size:122px;line-height:1;letter-spacing:-5px;
    transform:skewX(-8deg);color:var(--white);
  }
  .product-workout{
    position:absolute;left:284px;top:193px;width:270px;height:44px;
    font-family:"Exo 2",sans-serif;font-weight:900;font-style:italic;
    font-size:42px;line-height:44px;text-align:center;letter-spacing:-1px;
    transform:skewX(-8deg);color:var(--white);
  }
  .tagline{
    position:absolute;left:290px;top:244px;width:260px;text-align:center;
    font-family:"Exo 2",sans-serif;font-weight:900;font-style:italic;
    font-size:21px;line-height:21px;letter-spacing:.5px;
    color:var(--purple-bright);transform:skewX(-8deg);
  }
  .stat-row{position:absolute;left:288px;top:294px;display:flex;gap:10px}
  .stat{
    width:58px;height:34px;background:var(--purple);
    border-right:2px solid var(--lime);border-bottom:2px solid var(--lime);
    transform:skewX(-12deg);text-align:center;line-height:1;padding-top:3px;
  }
  .stat-value{font-family:"Exo 2",sans-serif;font-weight:800;font-style:italic;font-size:18px}
  .stat-value small{font-size:9px}
  .stat-name{display:block;font-size:5.5px;font-weight:700;letter-spacing:.3px;margin-top:1px}

  .net-weight{
    position:absolute;left:290px;top:345px;width:260px;text-align:center;
    font-size:10.5px;line-height:12px;letter-spacing:.5px;
  }
  .servings{
    position:absolute;left:392px;top:380px;width:108px;text-align:center;line-height:1;
    font-family:"Exo 2",sans-serif;font-weight:900;
  }
  .servings-count{display:block;font-size:46px;letter-spacing:3px}
  .servings-word{display:block;font-size:11px;letter-spacing:1.5px;margin-top:-3px}
  .line-name{
    position:absolute;left:590px;top:391px;font-family:"Exo 2",sans-serif;font-weight:900;
    font-style:italic;font-size:24px;letter-spacing:.5px;transform:skewX(-8deg);
  }

  .facts{
    position:absolute;left:57px;top:103px;width:160px;height:200px;background:var(--white);
    border-radius:5px;color:var(--ink);padding:5px 6px;font-size:4.3px;line-height:1.35;
  }
  .facts-title{font-family:"Oswald",sans-serif;font-weight:700;font-size:14px;line-height:16px;border-bottom:2px solid var(--ink)}
  .facts-meta{border-bottom:3px solid var(--ink);padding:1px 0}
  .facts-table{width:100%;border-collapse:collapse}
  .facts-table td{border-bottom:.5px solid #999;padding:.3px 0;font-weight:600}
  .facts-table td:nth-child(2){text-align:right}
  .facts-table td:nth-child(3){text-align:right;width:18px}
  .facts-table .head td{font-weight:400;font-size:3.6px;border-bottom:1.5px solid var(--ink)}
  .facts-table .sub td:first-child{padding-left:5px}
  .facts-foot{font-size:3.6px;border-top:2px solid var(--ink);padding-top:1px}
  .facts-other{margin-top:4px;font-size:4.2px}

  .text-block{position:absolute;font-size:8px;line-height:10px}
  .text-block h3{font-size:7.5px;font-weight:400;color:var(--purple-bright);letter-spacing:.5px;margin-bottom:2px}
  .other-ingredients{left:57px;top:330px;width:180px}
  .directions{left:630px;top:103px;width:170px}
  .directions p + h3{margin-top:10px}
</style>
</head>
<body>
<div class="canvas">
  <section class="label" aria-label="BROVEN Pre Workout flat label">
    <svg class="label-shapes" viewBox="0 0 824 446" aria-hidden="true">
      <polygon points="0,0 520,0 502,70 0,70" fill="var(--purple)"/>
      <g fill="var(--purple-bright)">
        <polygon points="530,0 543,0 528,42 515,42"/>
        <polygon points="554,0 567,0 552,42 539,42"/>
        <polygon points="578,0 591,0 576,42 563,42"/>
        <polygon points="602,0 615,0 600,42 587,42"/>
        <polygon points="626,0 639,0 624,42 611,42"/>
        <polygon points="650,0 663,0 648,42 635,42"/>
        <polygon points="674,0 687,0 672,42 659,42"/>
        <polygon points="698,0 711,0 696,42 683,42"/>
        <polygon points="722,0 735,0 720,42 707,42"/>
        <polygon points="746,0 759,0 744,42 731,42"/>
        <polygon points="770,0 783,0 768,42 755,42"/>
        <polygon points="794,0 807,0 792,42 779,42"/>
      </g>
      <polygon points="286,193 562,193 550,237 274,237" fill="var(--purple)"/>
      <polygon points="380,379 824,379 824,446 360,446" fill="var(--purple)"/>
      <g fill="var(--purple-bright)">
        <polygon points="44,404 56,404 42,446 30,446"/>
        <polygon points="66,404 78,404 64,446 52,446"/>
        <polygon points="88,404 100,404 86,446 74,446"/>
        <polygon points="110,404 122,404 108,446 96,446"/>
        <polygon points="132,404 144,404 130,446 118,446"/>
        <polygon points="154,404 166,404 152,446 140,446"/>
        <polygon points="176,404 188,404 174,446 162,446"/>
        <polygon points="198,404 210,404 196,446 184,446"/>
        <polygon points="220,404 232,404 218,446 206,446"/>
        <polygon points="242,404 254,404 240,446 228,446"/>
        <polygon points="264,404 276,404 262,446 250,446"/>
        <polygon points="286,404 298,404 284,446 272,446"/>
        <polygon points="308,404 320,404 306,446 294,446"/>
        <polygon points="330,404 342,404 328,446 316,446"/>
        <polygon points="352,404 364,404 350,446 338,446"/>
      </g>
    </svg>

    <div class="brand-name brand-top">BROVEN</div>

    <div class="facts">
      <div class="facts-title">SUPPLEMENT FACTS</div>
      <div class="facts-meta">Serving Size 1 scoop (32.0 g)<br>Servings Per Container 30</div>
      <table class="facts-table">
        <tr class="head"><td></td><td>Amount Per Serving</td><td>% DV</td></tr>
        <tr><td>Calories</td><td>8</td><td></td></tr>
        <tr><td>Total Carbohydrate</td><td>2.0 g</td><td>0.7%*</td></tr>
        <tr class="sub"><td>Hydroxypropyl distarch phosphate</td><td>1000 mg</td><td>**</td></tr>
        <tr class="sub"><td>Highly branched cyclic dextrin</td><td>10 mg</td><td>**</td></tr>
        <tr><td>Branched-Chain Amino Acids</td><td>7500 mg</td><td>**</td></tr>
        <tr class="sub"><td>L-Leucine</td><td>3000 mg</td><td>**</td></tr>
        <tr class="sub"><td>L-Isoleucine</td><td>3000 mg</td><td>**</td></tr>
        <tr class="sub"><td>L-Valine</td><td>1500 mg</td><td>**</td></tr>
        <tr><td>Creatine Monohydrate</td><td>5000 mg</td><td>**</td></tr>
        <tr><td>L-Citrulline</td><td>4300 mg</td><td>**</td></tr>
        <tr><td>Betaine Anhydrous</td><td>2500 mg</td><td>**</td></tr>
        <tr><td>Beta-Alanine</td><td>2400 mg</td><td>**</td></tr>
        <tr><td>Caffeine</td><td>350 mg</td><td>**</td></tr>
        <tr><td>Creatyl-L-Leucine [Prime Creatine]</td><td>250 mg</td><td>**</td></tr>
      </table>
      <div class="facts-foot">*Percent Daily Values based on a 2,000 calorie diet. **DV not established.</div>
      <div class="facts-other"><b>OTHER INGREDIENTS:</b> Cocoa powder (processed with alkali), natural and artificial flavors, sucralose, and lecithin.</div>
    </div>

    <div class="text-block other-ingredients">
      <h3>OTHER INGREDIENTS</h3>
      <p>Artificial Flavors, Polydextrose, Citric Acid, Malic Acid, Calcium Silicate, Silicon Dioxide, Sucralose, Acesulfame Potassium</p>
    </div>

    <h1 class="product-pre">PRE</h1>
    <h2 class="product-workout">WORKOUT</h2>
    <div class="tagline">PERFORMANCE<br>RECOVERY</div>

    <div class="stat-row">
      <div class="stat"><span class="stat-value">9<small>G</small></span><span class="stat-name">CITRULLINE</span></div>
      <div class="stat"><span class="stat-value">3<small>G</small></span><span class="stat-name">CREATINE</span></div>
      <div class="stat"><span class="stat-value">277<small>MG</small></span><span class="stat-name">CAFFEINE</span></div>
      <div class="stat"><span class="stat-value">3<small>G</small></span><span class="stat-name">BETA-ALANINE</span></div>
    </div>

    <div class="net-weight">DIETARY SUPPLEMENT<br>NET WT 195g (6.9 OZ)</div>

    <div class="servings"><span class="servings-count">30</span><span class="servings-word">SERVINGS</span></div>

    <div class="text-block directions">
      <h3>DIRECTIONS</h3>
      <p>Take one serving (1 level scoop) of BROVEN, mixed with 6 fl. oz of water, 20-30 minutes before training. Some individuals may experience a harmless tingling sensation, which is attributable to Beta-Alanine. Use only as directed.</p>
      <h3>NOTE:</h3>
      <p>Please do not use in combination with other dietary supplements, pharmaceuticals, foods that are considered to be stimulants.</p>
    </div>

    <div class="brand-name brand-bottom">BROVEN</div>
    <div class="line-name">PRE WORKOUT</div>
  </section>
</div>
</body>
</html>
```